Environmental Plastics Infographic on Marine Debris

We need a series of infographics that can be used individually or as a combined presentation. We'd like the combined piece to include an introduction and conclusion along with 4-5 infographics. Each infographic (information unit) should also work as a standalone. We are trying to help people visualize size proportions and ratios to put the plastics marine debris problem in perspective. Our key point is concerning polystyrene foam which represents 35 tons. We are looking for something creative to help people understand what the problem represents in terms they are familiar with.

To view our typical company design/style please see our website at www.brantleyfoamworks.org. Our primary RGB colors are: (187,140,9); (94,47,29); (94,138,164); and (164,167,15). Secondary RGB colors are (249,162,28) and (218,210,208). Our title/header font is DIN Next LT Pro and our copy font is Calibri 10.5 pt. We can deviate from the font specification if beneficial and welcome interesting text treatments and typography.

Need extra days to review

Target Market(s)

international brand manufacturers (corvantel, makiro), US legislators & government agencies

Font styles to use
Sans Serif

Requirements
Must have
• Sufficient white space. Easy to grasp message concept with visual components.

```html
<!DOCTYPE html>
<html lang="en">
<head>
<meta charset="utf-8">
<title>Polystyrene and Ocean Health</title>
<link href="https://fonts.googleapis.com/css2?family=Barlow+Condensed:wght@500;600;700&family=Carlito:wght@400;700&family=Libre+Baskerville:wght@700&display=swap" rel="stylesheet">
<style>
:root{
  --olive:#a0a318;
  --gold:#bb8c09;
  --orange:#f9a21c;
  --blue:#5e8aa4;
  --brown:#5e2f1d;
  --grey:#dad2d0;
  --ink:#222;
  --bell:#2b2b2b;
  --page:#e3ebe2;
}
*{box-sizing:border-box;margin:0;padding:0}
html,body{width:1066px;height:1200px;overflow:hidden}
body{background:var(--page);font-family:"Carlito",sans-serif;color:var(--ink);position:relative}
.panel{position:absolute;width:501px;height:376px;background:#fff;overflow:hidden;box-shadow:0 1px 4px rgba(0,0,0,.15)}
.abs{position:absolute}
.head{font-family:"Barlow Condensed",sans-serif;font-weight:700;color:#fff;text-align:center;line-height:1}
.ph{position:absolute}

/* intro */
.intro-band{left:0;top:0;width:100%;height:134px;background:var(--olive);display:flex;align-items:center;justify-content:center}
.intro-band h1{font-size:40px;line-height:1.2;white-space:nowrap}
.intro-copy{left:22px;top:158px;width:458px;font-size:8.4px;line-height:1.35}
.intro-copy a{color:#2a63b8}
.intro-stats{left:0;top:259px;width:100%;height:117px;background:var(--grey)}
.intro-stats .total{position:absolute;left:26px;top:16px;font-size:8.4px}
.intro-stats .total b{color:var(--gold);font-size:14px}
.stat{position:absolute;left:58px;font-size:8.2px;display:flex;align-items:center;gap:4px;white-space:nowrap}
.stat .pct{color:var(--gold);font-size:14.5px;font-weight:700}
.tick{width:13px;height:13px;border-radius:50%;background:var(--blue);display:inline-flex;align-items:center;justify-content:center;flex:none}
.tick svg{width:8px;height:8px}

/* sizing */
.news{left:10px;top:10px;width:170px;height:200px;background:#fff;box-shadow:0 1px 5px rgba(0,0,0,.3);padding:4px 4px;z-index:2}
.news .brand{font-family:"Carlito",sans-serif;font-weight:700;font-size:15px;display:flex;align-items:center;gap:4px}
.news .brand i{display:inline-block;width:14px;height:14px;border-radius:50%;background:#111}
.news .photo{margin-top:5px;height:86px;background:linear-gradient(#4d7fae,#1f4668)}
.news h3{font-family:"Libre Baskerville",serif;font-size:10.4px;line-height:1.15;margin-top:5px}
.news small{display:block;font-size:3.5px;color:#777;margin-top:3px}
.scale-label{font-family:"Barlow Condensed",sans-serif;font-weight:600;font-size:13px}
.scale-label.gold{color:var(--orange)}
.scale-label.blue{color:var(--blue)}
.sizing-band{left:0;top:164px;width:100%;height:212px;background:var(--olive)}
.sizing-title{left:190px;top:170px;font-family:"Barlow Condensed",sans-serif;font-weight:700;font-size:33px;color:var(--blue)}
.size-row{position:absolute;left:0;width:100%;height:20px}
.size-row .bag{position:absolute;left:40px;top:-12px;width:50px;height:34px;border-radius:45% 45% 40% 40%;background:#222;color:var(--orange);font-size:10.5px;font-weight:700;display:flex;align-items:flex-end;justify-content:center;padding-bottom:4px}
.size-row .name{position:absolute;left:200px;width:120px;text-align:center;font-family:"Barlow Condensed",sans-serif;font-weight:700;font-size:15px;color:#fff}
.size-row .val{position:absolute;right:28px;font-family:"Barlow Condensed",sans-serif;font-weight:700;font-size:15px;color:#fff}
.rule{position:absolute;left:110px;width:364px;border-top:1px dashed rgba(255,255,255,.8)}

/* how big */
.big-band{left:0;top:0;width:100%;height:51px;background:var(--olive);display:flex;align-items:center;justify-content:center}
.big-band h2{font-size:39px;font-weight:600}
.compare-band{left:0;top:119px;width:100%;height:56px;background:var(--olive)}
.brown-rule{left:0;top:175px;width:100%;height:6px;background:var(--brown)}
.cmp-label{position:absolute;top:61px;text-align:center;font-family:"Barlow Condensed",sans-serif;font-weight:600;font-size:11.5px;line-height:1.35;z-index:2}
.cmp-label span{display:block;color:var(--orange);font-weight:500}
.cmp-pct{position:absolute;top:150px;color:#fff;font-weight:700;font-size:12.5px;text-align:center;z-index:2}
.col{position:absolute;top:200px;height:155px;text-align:center}
.col .icon{margin:0 auto;height:30px;border-radius:4px}
.col .cap{font-size:8px;color:var(--blue);margin-top:14px}
.p4 .col .cap{color:#333}
.col .tons{font-family:"Barlow Condensed",sans-serif;font-weight:600;font-size:15px;color:var(--gold);margin-top:22px}
.bells{display:flex;gap:5px;justify-content:center;margin-top:18px;overflow:hidden;height:26px}
.bell{position:relative;flex:none;width:24px;height:20px;margin-top:6px;border-radius:50% 50% 40% 40%;background:var(--bell);color:var(--orange);font-size:8px;font-weight:700;display:flex;align-items:center;justify-content:center}
.bell::before{content:"";position:absolute;top:-6px;left:5px;width:14px;height:9px;border:3px solid var(--bell);border-bottom:none;border-radius:7px 7px 0 0}
.divider{position:absolute;top:200px;height:155px;border-left:1px dashed var(--olive)}

/* eps */
.eps-band{left:0;top:0;width:100%;height:58px;background:var(--olive);display:flex;align-items:center;justify-content:center}
.eps-band h2{font-size:27px;font-weight:600}
.map{left:30px;top:90px;width:440px;height:270px;background:radial-gradient(ellipse at center,#e9ecd0 0%,#f3f5e6 70%,#fff 100%);border-radius:30px}
.disc{position:absolute;border-radius:50%;color:#fff;text-align:center;display:flex;flex-direction:column;align-items:center;justify-content:center;padding:6px}
.disc small{font-size:5.6px;line-height:1.2;opacity:.9}
.disc b{font-weight:400;font-size:13px;margin-top:2px}
.disc.olive{background:var(--olive);opacity:.95}
.disc.blue{background:var(--blue);opacity:.95}
.disc.gold{background:var(--gold);opacity:.95}
.disc.gold b{font-size:10px}

/* discoveries */
.disc-band{left:0;top:0;width:100%;height:66px;background:var(--olive);display:flex;align-items:center;justify-content:center}
.disc-band h2{font-size:40px;font-weight:600}
.find{position:absolute;left:26px;display:flex;align-items:center;gap:13px;font-size:13.4px}
.find .tick{width:25px;height:25px}
.find .tick svg{width:13px;height:13px}
.closing-title{left:26px;top:235px;font-weight:700;font-size:16px;color:var(--blue)}
.closing{left:26px;top:256px;width:340px;font-size:12.4px;line-height:1.36;z-index:2;white-space:nowrap}
.closing em{font-style:normal;color:var(--olive)}
.source{left:26px;top:325px;font-size:5.6px;z-index:2}
.source a{color:#2a63b8}
.bag-stat{left:356px;top:268px;width:134px;height:92px;border-radius:46% 46% 38% 38%;background:#232323;color:#fff;text-align:center;padding-top:12px;z-index:1}
.bag-stat .j{font-size:10px}
.bag-stat .n{font-size:19px;font-weight:700;color:var(--orange)}
.bag-stat .t{font-size:7.5px;line-height:1.2}
.foot-band{left:0;top:351px;width:100%;height:25px;background:var(--olive)}
</style>
</head>
<body>

<!-- Intro -->
<section class="panel" style="left:18px;top:16px">
  <div class="abs intro-band"><h1 class="head">HOW WILL POLYSTYRENE BANS<br>IMPROVE OCEAN HEALTH?</h1></div>
  <div class="abs intro-copy">
    <p>A recent <a href="#">report</a> looks at the role plastics play in marine debris that sheds light on previous assumptions about how different plastics contribute to the problem and where its coming from.</p>
    <p>In this ground breaking study, scientists conducted cutting-edge research at a much larger scale than had ever been done before. Over the course of three years, an international team including The Open Tide Foundation, six universities, and an aerial sensor company, collected data and mapped debris fields for the Great Pacific Garbage Patch, one of the most problematic plastic pollution hot spots.</p>
    <p>Polystyrene ban legislation imply product restrictions will minimize plastic marine debris. Let's take a closer look.</p>
  </div>
  <div class="abs intro-stats">
    <p class="total">The total plastics mass in the GPGP is projected at <b>78,908 tons.</b></p>
    <p class="stat" style="top:40px"><span class="tick"><svg viewBox="0 0 10 10"><path d="M1.5 5.2l2.3 2.3 4.7-5" fill="none" stroke="#fff" stroke-width="1.8"/></svg></span><span class="pct">52%</span><span>is mostly <b>abandoned fishing gear</b>, not consumer plastics.</span></p>
    <p class="stat" style="top:64px"><span class="tick"><svg viewBox="0 0 10 10"><path d="M1.5 5.2l2.3 2.3 4.7-5" fill="none" stroke="#fff" stroke-width="1.8"/></svg></span><span class="pct">47%</span><span>is <b>hard plastics, sheets and film</b>, making up the majority of the microplastics mass.</span></p>
    <p class="stat" style="top:88px"><span class="tick"><svg viewBox="0 0 10 10"><path d="M1.5 5.2l2.3 2.3 4.7-5" fill="none" stroke="#fff" stroke-width="1.8"/></svg></span><span class="pct">0,05%</span><span>is <b>foamed plastics</b> – including polystyrene – making it a minor component of the GPGP.</span></p>
  </div>
</section>

<!-- Sizing it up -->
<section class="panel" style="left:542px;top:16px">
  <div class="abs sizing-band"></div>
  <div class="abs news">
    <div class="brand"><i></i>CIVIC NEWSDESK</div>
    <div class="photo" role="img" aria-label="Photo of research vessel rigging over the open ocean"></div>
    <h3>Great Pacific Garbage Patch weighs more than 43,000 cars and is much larger than we thought</h3>
    <small>Science · Mar 22, 2018 10:00 AM EDT · Updated Apr 18</small>
  </div>
  <span class="abs scale-label gold" style="left:240px;top:22px">Total GPGP Mass</span>
  <span class="abs scale-label gold" style="left:364px;top:22px">43,000 Cars</span>
  <div class="ph" style="left:242px;top:50px;width:184px;height:72px;background:linear-gradient(#cfd9e0,#9fb3c1);border-radius:6px" role="img" aria-label="Balance scale weighing a plastic debris pile against a car"></div>
  <span class="abs scale-label blue" style="left:222px;top:126px">Total Foam Plastic Mass</span>
  <span class="abs scale-label blue" style="left:378px;top:128px">18 Cars</span>
  <div class="abs sizing-title">SIZING IT UP</div>
  <div class="size-row" style="top:238px"><span class="bag" role="img" aria-label="Rubbish bag">42 tons</span><span class="name">MEGAPLASTICS</span><span class="val">&gt;50 cm</span></div>
  <div class="rule" style="top:257px"></div>
  <div class="size-row" style="top:275px"><span class="bag" role="img" aria-label="Rubbish bag">20 tons</span><span class="name">MACROPLASTICS</span><span class="val">5 – 50 cm</span></div>
  <div class="rule" style="top:295px"></div>
  <div class="size-row" style="top:314px"><span class="bag" role="img" aria-label="Rubbish bag">10 tons</span><span class="name">MESOPLASTICS</span><span class="val">0.5 – 5 cm</span></div>
  <div class="rule" style="top:333px"></div>
  <div class="size-row" style="top:354px"><span class="bag" role="img" aria-label="Rubbish bag">6,5 tons</span><span class="name">MICROPLASTICS</span><span class="val">0.05 – 0.5 cm</span></div>
</section>

<!-- How big is big (photo version) -->
<section class="panel" style="left:18px;top:409px">
  <div class="abs big-band"><h2 class="head">How Big is BIG?</h2></div>
  <div class="abs compare-band"></div>
  <div class="abs brown-rule"></div>
  <p class="cmp-label" style="left:40px;width:100px;text-align:left">1 Cruise Ship<span>100,000 tons</span></p>
  <p class="cmp-label" style="left:219px;width:100px;text-align:left">1 Blue Whale<span>150,000 tons</span></p>
  <p class="cmp-label" style="left:350px;width:150px">1 Week NYC Waste Generation<span>269,230 tons</span></p>
  <div class="ph" style="left:34px;top:100px;width:100px;height:45px;background:linear-gradient(#e9eef3,#9aa9b8);border-radius:8px" role="img" aria-label="Cruise ship photo"></div>
  <div class="ph" style="left:176px;top:100px;width:130px;height:32px;background:linear-gradient(#a7bfd0,#5f7f98);border-radius:50%" role="img" aria-label="Blue whale illustration"></div>
  <div class="ph" style="left:338px;top:92px;width:150px;height:56px;background:linear-gradient(#c3cfd9,#4c5e70);border-radius:4px" role="img" aria-label="New York skyline with garbage truck"></div>
  <p class="cmp-pct" style="left:30px;width:90px">GPGP = 79%</p>
  <p class="cmp-pct" style="left:190px;width:90px">GPGP = 53%</p>
  <p class="cmp-pct" style="left:389px;width:90px">GPGP = 29%</p>
  <div class="divider" style="left:117px"></div>
  <div class="divider" style="left:228px"></div>
  <div class="divider" style="left:349px"></div>
  <div class="col" style="left:10px;width:100px"><div class="icon" style="width:64px;background:linear-gradient(#8ea2b5,#34475a)" role="img" aria-label="Pile of plastic debris"></div><p class="cap">All GPGP Plastics</p><p class="tons">78,908 tons</p><div class="bells" style="width:46px;margin-left:auto;margin-right:auto;justify-content:flex-start"><span class="bell">50</span><span class="bell">50</span></div></div>
  <div class="col" style="left:122px;width:102px"><div class="icon" style="width:60px;background:linear-gradient(#e1e6ea,#8795a3)" role="img" aria-label="Cruise ship"></div><p class="cap">1 Cruise Ship</p><p class="tons">100,000 tons</p><div class="bells"><span class="bell">50</span><span class="bell">50</span></div></div>
  <div class="col" style="left:232px;width:114px"><div class="icon" style="width:70px;background:linear-gradient(#a7bfd0,#5f7f98)" role="img" aria-label="Blue whale"></div><p class="cap">1 Blue Whale</p><p class="tons">200,000 tons</p><div class="bells"><span class="bell">50</span><span class="bell">50</span><span class="bell">50</span><span class="bell">50</span></div></div>
  <div class="col" style="left:354px;width:143px"><div class="icon" style="width:76px;background:linear-gradient(#c3cfd9,#4c5e70)" role="img" aria-label="City skyline with truck"></div><p class="cap">1 Week NYC City Waste Generation</p><p class="tons">269,230 tons</p><div class="bells" style="justify-content:flex-start;padding-left:10px"><span class="bell">50</span><span class="bell">50</span><span class="bell">50</span><span class="bell">50</span><span class="bell">50</span></div></div>
</section>

<!-- How big is big (flat version) -->
<section class="panel p4" style="left:542px;top:409px">
  <div class="abs big-band"><h2 class="head">How Big is BIG?</h2></div>
  <div class="abs compare-band"></div>
  <div class="abs brown-rule"></div>
  <p class="cmp-label" style="left:40px;width:100px;top:66px">1 Cruise Ship<span>100,000 tons</span></p>
  <p class="cmp-label" style="left:210px;width:100px">1 Blue Whale<span>150,000 tons</span></p>
  <p class="cmp-label" style="left:350px;width:150px">1 Week NYC Waste Generation<span>269,230 tons</span></p>
  <div class="ph" style="left:20px;top:118px;width:134px;height:24px;background:linear-gradient(#fff,#dfe6ec);border-radius:3px" role="img" aria-label="Flat cruise ship drawing"></div>
  <div class="ph" style="left:218px;top:96px;width:44px;height:50px;background:linear-gradient(#c9d6df,#6f8799);border-radius:40% 40% 10% 10%" role="img" aria-label="Flat whale tail drawing"></div>
  <div class="ph" style="left:378px;top:96px;width:80px;height:52px;background:linear-gradient(#e7b24a,#c58a1e);border-radius:4px" role="img" aria-label="Flat city and truck drawing"></div>
  <p class="cmp-pct" style="left:33px;width:90px;top:144px">GPGP = 79%</p>
  <p class="cmp-pct" style="left:195px;width:90px">GPGP = 53%</p>
  <p class="cmp-pct" style="left:380px;width:90px">GPGP = 29%</p>
  <div class="divider" style="left:117px"></div>
  <div class="divider" style="left:228px"></div>
  <div class="divider" style="left:349px"></div>
  <div class="col" style="left:10px;width:100px"><div class="icon" style="width:64px;background:linear-gradient(#8ea2b5,#34475a)" role="img" aria-label="Pile of plastic debris"></div><p class="cap">All GPGP Plastics</p><p class="tons">78,908 tons</p><div class="bells" style="width:46px;margin-left:auto;margin-right:auto;justify-content:flex-start"><span class="bell">50</span><span class="bell">50</span></div></div>
  <div class="col" style="left:122px;width:102px"><div class="icon" style="width:80px;height:20px;margin-top:10px;background:linear-gradient(#fff,#cdd6de)" role="img" aria-label="Cruise ship"></div><p class="cap">1 Cruise Ship</p><p class="tons">100,000 tons</p><div class="bells"><span class="bell">50</span><span class="bell">50</span></div></div>
  <div class="col" style="left:232px;width:114px;top:190px"><div class="icon" style="width:40px;height:52px;background:linear-gradient(#c9d6df,#6f8799)" role="img" aria-label="Whale tail"></div><p class="cap" style="margin-top:2px">1 Blue Whale</p><p class="tons">200,000 tons</p><div class="bells"><span class="bell">50</span><span class="bell">50</span><span class="bell">50</span><span class="bell">50</span></div></div>
  <div class="col" style="left:354px;width:143px;top:190px"><div class="icon" style="width:60px;height:52px;background:linear-gradient(#e7b24a,#c58a1e)" role="img" aria-label="City and truck"></div><p class="cap" style="margin-top:2px">1 Week NYC City Waste Generation</p><p class="tons">269,230 tons</p><div class="bells" style="justify-content:flex-start;padding-left:10px"><span class="bell">50</span><span class="bell">50</span><span class="bell">50</span><span class="bell">50</span><span class="bell">50</span></div></div>
</section>

<!-- EPS waste -->
<section class="panel" style="left:18px;top:801px">
  <div class="abs eps-band"><h2 class="head">HOW MUCH MISMANAGED EPS WASTE WAS FOUND?</h2></div>
  <div class="ph map" role="img" aria-label="Faint world map"></div>
  <div class="disc olive" style="left:30px;top:98px;width:112px;height:112px"><small>Worldwide Annual Plastics Production</small><b>320,000,000 tons</b></div>
  <div class="disc blue" style="left:63px;top:174px;width:100px;height:100px"><small>Total GPGP Plastics</small><b>78,908 tons</b></div>
  <div class="disc gold" style="left:85px;top:238px;width:88px;height:88px"><small>Percent of Global Production in GPGP</small><b>0.000024%</b></div>
  <div class="disc olive" style="left:359px;top:98px;width:112px;height:112px"><small>Worldwide Expanded Polystyrene (EPS) Plastics Production</small><b>6,620,000 tons</b></div>
  <div class="disc blue" style="left:342px;top:177px;width:100px;height:100px"><small>Total GPGP Foam Plastics</small><b>35 tons</b></div>
  <div class="disc gold" style="left:317px;top:239px;width:88px;height:88px"><small>Percent of Global Production in GPGP</small><b>0.0000053%</b></div>
</section>

<!-- Discoveries -->
<section class="panel" style="left:542px;top:801px">
  <div class="abs disc-band"><h2 class="head">SURPRISING DISCOVERIES</h2></div>
  <p class="find" style="top:106px"><span class="tick"><svg viewBox="0 0 10 10"><path d="M1.5 5.2l2.3 2.3 4.7-5" fill="none" stroke="#fff" stroke-width="1.8"/></svg></span>Approximately 50% of GPGP Plastics are From Marine-Based Sources.</p>
  <p class="find" style="top:145px"><span class="tick"><svg viewBox="0 0 10 10"><path d="M1.5 5.2l2.3 2.3 4.7-5" fill="none" stroke="#fff" stroke-width="1.8"/></svg></span>Beach Litter Studies Were Not Indicative of GPGP Content.</p>
  <p class="find" style="top:183px"><span class="tick"><svg viewBox="0 0 10 10"><path d="M1.5 5.2l2.3 2.3 4.7-5" fill="none" stroke="#fff" stroke-width="1.8"/></svg></span>20% of the GPGP Plastic Debris Is From the 2011 Tohoku Tsunami</p>
  <p class="abs closing-title">All Marine Plastic Debris Is A Problem!</p>
  <p class="abs closing">However, plastic product bans will be ineffective in reducing<br>ocean debris. Since the U.S. contributes just <em>0.9%</em> of the<br>World's Mismanaged Plastic Waste<sup>1</sup>, it is even more<br>important to consider all parts of equation.</p>
  <p class="abs source"><sup>1</sup>Source: <a href="#">6 things you can do to stop plastic pollution today</a>, Daily Ledger, September 7, 2018</p>
  <div class="abs foot-band"></div>
  <div class="abs bag-stat"><p class="j">just</p><p class="n">0.90%</p><p class="t">World's Mismanaged Plastic<br>Waste</p></div>
</section>

</body>
</html>
```